Dental Office Business Card

We need a business card for our pediatric dentistry office.
On one side the design needs to contain the following:
our logo (attached)
Vento Pediatric Grins
Soraya Kadbelani, DDS
Board Certified Pediatric Dentist
Tel: (555) 318-2747)
Fax: (555) 264-8031
Email: info@ventopediatricgrins.example
Web: www.ventopediatricgrins.example
Address: 41 Brindle Ave, Suite 208, Marrowdale, ST 02099

On the other side of the card, the design needs to have an appointment reminder (date and time as well as day of the week) similar to the design attached (no need for appointment reason “For”)

```html
<!DOCTYPE html>
<html lang="en">
<head>
<meta charset="utf-8">
<title>Vento Pediatric Grins – Business Card</title>
<link rel="stylesheet" href="https://fonts.googleapis.com/css2?family=Montserrat:wght@500;600;700&family=Arimo:wght@400&family=Michroma&display=swap">
<style>
  :root {
    --stage: #0b100b;
    --green: #568a55;
    --green-dark: #41703f;
    --green-light: #a9d6a6;
    --white: #ffffff;
    --ink: #111111;
    --ghost: #ececec;
  }
  * { margin: 0; padding: 0; box-sizing: border-box; }
  html, body { width: 1200px; height: 1000px; overflow: hidden; background: var(--stage); }
  .canvas { position: relative; width: 1200px; height: 1000px; }

  .card { position: absolute; left: 204px; width: 794px; height: 453px; border-radius: 18px; overflow: hidden; }
  .card--front { top: 34px; background: var(--green); color: var(--white); }
  .card--back { top: 512px; background: var(--white); color: var(--green-dark); }

  /* Front */
  .brand { position: absolute; left: 36px; top: 38px; display: flex; align-items: center; gap: 14px; }
  .brand__dot { width: 58px; height: 58px; border-radius: 50%; background: var(--green-light); }
  .brand__name { font-family: "Montserrat", sans-serif; font-weight: 600; font-size: 27px; color: var(--white); line-height: 1; }

  .mark-area { position: absolute; left: 470px; top: 30px; width: 300px; height: 240px; border-radius: 50%;
    background: radial-gradient(circle at 50% 50%, var(--green-light) 0%, #7fb27d 60%, rgba(86,138,85,0) 72%); }

  .identity { position: absolute; left: 33px; top: 178px; }
  .identity__office { font-family: "Montserrat", sans-serif; font-weight: 700; font-size: 29.5px; letter-spacing: 0.3px; line-height: 1; margin-bottom: 2px; }
  .identity__line { font-family: "Arimo", sans-serif; font-size: 20px; line-height: 30px; }

  .divider { position: absolute; left: 33px; right: 35px; top: 286px; height: 1.5px; background: var(--white); }

  .contact { position: absolute; display: flex; align-items: center; gap: 11px; font-family: "Arimo", sans-serif; font-size: 20px; }
  .contact__icon { width: 26px; height: 26px; border-radius: 4px; background: var(--ink); display: flex; align-items: center; justify-content: center; }
  .contact__icon svg { width: 16px; height: 16px; fill: var(--white); }
  .contact--tel { left: 33px; top: 310px; }
  .contact--fax { left: 33px; top: 344px; }
  .contact--mail { left: 422px; top: 310px; }
  .contact--web { left: 422px; top: 344px; }

  .address { position: absolute; left: 0; right: 0; top: 404px; display: flex; justify-content: center; align-items: center; gap: 8px;
    font-family: "Montserrat", sans-serif; font-weight: 500; font-size: 17px; text-transform: uppercase; }
  .address svg { width: 18px; height: 22px; fill: var(--white); }

  /* Back */
  .reminder-title { position: absolute; left: 0; right: 0; top: 18px; text-align: center; font-family: "Michroma", sans-serif;
    font-size: 46px; letter-spacing: 4px; color: var(--green-dark); line-height: 1.2;
    -webkit-text-stroke: 1.6px var(--green-dark); }
  .reminder-band { position: absolute; left: 35px; right: 35px; top: 80px; height: 33px; border-radius: 6px; background: var(--green);
    display: flex; align-items: center; justify-content: center; gap: 10px; }
  .reminder-band__text { font-family: "Michroma", sans-serif; font-size: 21px; letter-spacing: 3px; color: var(--white);
    -webkit-text-stroke: 0.8px var(--white); }
  .reminder-band__dot { width: 12px; height: 12px; border-radius: 50%; background: var(--white); }

  .ghost-mark { position: absolute; left: 228px; top: 140px; width: 340px; height: 290px; border-radius: 50%;
    background: radial-gradient(circle, var(--ghost) 0%, rgba(236,236,236,0.6) 55%, rgba(255,255,255,0) 72%); }

  .field { position: absolute; left: 35px; display: flex; align-items: flex-end; font-family: "Arimo", sans-serif; font-size: 27px; color: var(--green-dark); }
  .field__label { width: 103px; line-height: 1; }
  .field__line { height: 2px; background: var(--green-dark); margin-bottom: 4px; }
  .field--for { top: 168px; }
  .field--date { top: 231px; }
  .field--for .field__line, .field--date .field__line { width: 621px; }
  .field--time { top: 380px; }
  .field--time .field__line { width: 282px; }
  .field__suffix { font-size: 21px; margin-left: 21px; word-spacing: 6px; margin-bottom: -2px; }

  .days { position: absolute; left: 35px; right: 34px; top: 307px; display: flex; justify-content: space-between; }
  .day { display: flex; align-items: center; gap: 9px; font-family: "Arimo", sans-serif; font-size: 24px; color: var(--green-dark); }
  .day__box { width: 30px; height: 30px; border: 2px solid var(--green-dark); border-radius: 3px; background: var(--white); }
</style>
</head>
<body>
<main class="canvas">

  <section class="card card--front">
    <div class="brand">
      <span class="brand__dot"></span>
      <span class="brand__name">Vento Pediatric Grins</span>
    </div>
    <div class="mark-area" role="img" aria-label="Brand symbol decoration"></div>

    <div class="identity">
      <h1 class="identity__office">VENTO PEDIATRIC GRINS</h1>
      <p class="identity__line">Soraya Kadbelani, DDS</p>
      <p class="identity__line">Board Certified Pediatric Dentist</p>
    </div>

    <div class="divider"></div>

    <div class="contact contact--tel">
      <span class="contact__icon"><svg viewBox="0 0 16 16"><path d="M5 1h6a1 1 0 0 1 1 1v12a1 1 0 0 1-1 1H5a1 1 0 0 1-1-1V2a1 1 0 0 1 1-1zm0.5 1.5v9h5v-9zM8 12.3a.8.8 0 1 0 0 1.6.8.8 0 0 0 0-1.6z"/></svg></span>
      <span>(555) 318-2747)</span>
    </div>
    <div class="contact contact--fax">
      <span class="contact__icon"><svg viewBox="0 0 16 16"><path d="M4 1h8v4H4zM2 6h12a1 1 0 0 1 1 1v5h-3v3H4v-3H1V7a1 1 0 0 1 1-1zm3 5v3h6v-3zm7-3.5a.8.8 0 1 0 0 1.6.8.8 0 0 0 0-1.6z"/></svg></span>
      <span>(555) 264-8031</span>
    </div>
    <div class="contact contact--mail">
      <span class="contact__icon"><svg viewBox="0 0 16 16"><path d="M15 1 1 7l4.5 1.8L13 3.5 7 10v4.5l2.5-3.2L13 13z"/></svg></span>
      <span>info@ventopediatricgrins.example</span>
    </div>
    <div class="contact contact--web">
      <span class="contact__icon"><svg viewBox="0 0 16 16"><path d="M8 1a7 7 0 1 0 0 14A7 7 0 0 0 8 1zm5.4 6.2h-2.5a11 11 0 0 0-1-4.3 5.5 5.5 0 0 1 3.5 4.3zM8 2.6c.6.9 1.2 2.6 1.3 4.6H6.7C6.8 5.2 7.4 3.5 8 2.6zM6.1 2.9a11 11 0 0 0-1 4.3H2.6a5.5 5.5 0 0 1 3.5-4.3zM2.6 8.8h2.5a11 11 0 0 0 1 4.3 5.5 5.5 0 0 1-3.5-4.3zM8 13.4c-.6-.9-1.2-2.6-1.3-4.6h2.6c-.1 2-.7 3.7-1.3 4.6zm1.9-.3a11 11 0 0 0 1-4.3h2.5a5.5 5.5 0 0 1-3.5 4.3z"/></svg></span>
      <span>www.ventopediatricgrins.example</span>
    </div>

    <p class="address">
      <svg viewBox="0 0 18 22"><path d="M9 0a8 8 0 0 0-8 8c0 6 8 14 8 14s8-8 8-14a8 8 0 0 0-8-8zm0 11a3 3 0 1 1 0-6 3 3 0 0 1 0 6z"/></svg>
      <span>41 Brindle Ave, Suite 208, Marrowdale, ST 02099</span>
    </p>
  </section>

  <section class="card card--back">
    <h2 class="reminder-title">APPOINTMENT</h2>
    <div class="reminder-band">
      <span class="reminder-band__dot"></span>
      <span class="reminder-band__text">REMINDER</span>
      <span class="reminder-band__dot"></span>
    </div>

    <div class="ghost-mark" role="img" aria-label="Faint brand symbol watermark"></div>

    <div class="field field--for"><span class="field__label">FOR&nbsp;&nbsp;:</span><span class="field__line"></span></div>
    <div class="field field--date"><span class="field__label">DATE :</span><span class="field__line"></span></div>

    <div class="days">
      <span class="day"><span class="day__box"></span>Mon</span>
      <span class="day"><span class="day__box"></span>Tue</span>
      <span class="day"><span class="day__box"></span>Wed</span>
      <span class="day"><span class="day__box"></span>Thu</span>
      <span class="day"><span class="day__box"></span>Fri</span>
      <span class="day"><span class="day__box"></span>Sat</span>
      <span class="day"><span class="day__box"></span>Sun</span>
    </div>

    <div class="field field--time"><span class="field__label">TIME&nbsp;&nbsp;:</span><span class="field__line"></span><span class="field__suffix">a.m. p.m.</span></div>
  </section>

</main>
</body>
</html>
```